I need a business card design for a new company that will be doing consulting work around issues of cultural competency, and diversity and inclusion. I would like the design to be crisp and clear with bold but conservative colors and incorporate shades of blue

Target Market(s)

Small businesses, schools, non-profits

Industry/Entity Type

Consulting

Font styles to use
Serif
Sans Serif

Colors
0c5ba6
6b449b
3276b5
0292cd

Requirements
Must have
• A Morrow Venture (name of company)
• Lemlem Tavish
• CEO
• lemlem@amorrowventure.com
• (215)483-2756

```html
<!DOCTYPE html>
<html lang="en">
<head>
<meta charset="utf-8">
<title>A Morrow Venture — Business Card</title>
<link rel="stylesheet" href="https://fonts.googleapis.com/css2?family=Quantico:wght@700&family=Advent+Pro:wght@200;300&display=swap">
<style>
  :root {
    --page: #ffffff;
    --card-edge: #2b2b2b;
    --deep-blue: #0e5ca8;
    --sky-blue: #19adf5;
    --ocean-blue: #0a8fd0;
    --aqua: #00ffff;
    --navy-line: #0a1f6b;
    --paper: #ffffff;
    --ink: #111111;
    --soft-ink: #6f6f6f;
  }
  * { box-sizing: border-box; margin: 0; padding: 0; }
  html, body {
    width: 1200px;
    height: 1200px;
    overflow: hidden;
    background: var(--page);
  }
  .business-card {
    position: absolute;
    left: 50px;
    top: 293px;
    width: 1100px;
    height: 614px;
    background: var(--paper);
    border: 1px solid var(--card-edge);
    overflow: hidden;
  }
  .block { position: absolute; }
  .block--deep {
    left: 0; top: 0; width: 548px; height: 308px;
    background: var(--deep-blue);
  }
  .block--sky {
    left: 53px; top: 85px; width: 495px; height: 223px;
    background: var(--sky-blue);
    border: 3px solid var(--navy-line);
    border-right: none;
    border-bottom: none;
  }
  .block--ocean {
    left: 548px; top: 308px; width: 552px; height: 306px;
    background: var(--ocean-blue);
  }
  .block--aqua {
    left: 548px; top: 308px; width: 508px; height: 242px;
    background: var(--aqua);
    border-right: 3px solid var(--navy-line);
    border-bottom: 3px solid var(--navy-line);
  }
  .company-name {
    position: absolute;
    left: 0; top: 124px; width: 1100px;
    text-align: center;
    font-family: "Quantico", sans-serif;
    font-weight: 700;
    font-size: 78px;
    line-height: 1;
    letter-spacing: 7px;
    text-transform: uppercase;
    color: var(--ink);
  }
  .title-rule {
    position: absolute;
    left: 415px; top: 236px; width: 268px; height: 4px;
    background: var(--ink);
  }
  .contact-line {
    position: absolute;
    width: 1100px;
    text-align: center;
    font-family: "Advent Pro", sans-serif;
    font-weight: 300;
    font-size: 46px;
    line-height: 1;
    color: var(--soft-ink);
  }
  .contact-line span { display: inline-block; }
  .contact-line--name { left: -172px; top: 286px; }
  .contact-line--role { left: -187px; top: 339px; }
  .contact-line--name span,
  .contact-line--role span {
    background: var(--paper);
    padding: 3px 10px 4px;
  }
  .contact-line--email { left: -40px; top: 392px; letter-spacing: 1px; }
  .contact-line--phone { left: -42px; top: 458px; letter-spacing: 1px; }
</style>
</head>
<body>
  <main class="business-card">
    <div class="block block--deep"></div>
    <div class="block block--sky"></div>
    <div class="block block--ocean"></div>
    <div class="block block--aqua"></div>

    <h1 class="company-name">A Morrow Venture</h1>
    <div class="title-rule"></div>

    <p class="contact-line contact-line--name"><span>Lemlem Tavish</span></p>
    <p class="contact-line contact-line--role"><span>CEO</span></p>
    <p class="contact-line contact-line--email"><span>lemlem@amorrowventure.com</span></p>
    <p class="contact-line contact-line--phone"><span>(215)483-2756</span></p>
  </main>
</body>
</html>
```